Business Card Design for a Jockey's Agent

A business card design that helps to develop a brand or identity for myself, the agent, perhaps on one side with a clean minimalist design, and on the other side a simple design with the two jockeys names i currently represent. Those jockeys may change twice a year as they move around the country, switch agents, etc, so i think keeping one side designed to promote the agent and a second side that can be changed easily to identify the jockeys i currently represent would be the best.

Target Market(s)

Thoroughbred racehorse trainers

Industry/Entity Type

Business

Contact Information for Business Card

Garrett Lindqvist - Jockey Agent
mobile (614) 382 7291
garrettplindqvist7mailhub.example

Jockeys: Everett Kline, Tobias Renwick

Font styles to use
Serif

Requirements
Must have
• contact info and modern feel and font
Nice to have
• clean minimalist element of racing, jockey silk, helmut or crop, finish marker pole from racetrack etc,
Should not have
• DONT HAVE ANY KIND OF LOGO ETC. IMAGE IS ONE OF MY RACEHORSES TO HELP FINISH BRIEF.
• racing horse, stuffy vintage racing feel or Weekly Paddock Sheet fonts

```html
<!DOCTYPE html>
<html lang="en">
<head>
<meta charset="utf-8">
<title>Garrett Lindqvist – Jockey Agent Business Card</title>
<link rel="stylesheet" href="https://fonts.googleapis.com/css2?family=Source+Serif+4:opsz,wght@8..60,400;8..60,500&display=swap">
<style>
  :root {
    --racing-red: #a51f24;
    --racing-red-deep: #8c1a1e;
    --sketch-red: #b5473c;
    --sketch-pink: #ecc9c4;
    --ink: #111111;
    --paper: #ffffff;
    --backdrop: #f1f0ee;
    --card-edge: #d9d6d2;
  }
  * { box-sizing: border-box; margin: 0; padding: 0; }
  html, body { width: 960px; height: 1200px; overflow: hidden; }
  body {
    background: var(--backdrop);
    font-family: "Source Serif 4", Georgia, serif;
    position: relative;
  }

  /* Jockeys side */
  .card-jockeys {
    position: absolute; left: 130px; top: 34px;
    width: 700px; height: 400px;
    background: var(--racing-red);
    color: var(--paper);
    box-shadow: 0 2px 6px rgba(0,0,0,.18);
    overflow: hidden;
  }
  .card-jockeys .heading {
    position: absolute; top: 40px; left: 0; width: 100%;
    text-align: center; font-size: 30px; font-weight: 400;
  }
  .card-jockeys .crossed-crops {
    position: absolute; left: 318px; top: 84px; width: 64px; height: 64px;
  }
  .jockey {
    position: absolute; top: 162px; width: 260px; text-align: center;
  }
  .jockey .name { font-size: 30px; font-weight: 400; line-height: 1.1; }
  .jockey .weight { font-size: 17px; margin-top: 4px; }
  .jockey-left { left: 46px; }
  .jockey-right { left: 400px; }
  .card-jockeys .horse-sketch {
    position: absolute; left: 90px; top: 150px; width: 520px; height: 250px;
    background: radial-gradient(ellipse at 55% 80%, var(--racing-red-deep) 0%, var(--racing-red) 75%);
    border-radius: 45% 45% 0 0 / 60% 60% 0 0;
    opacity: .9;
  }

  /* Agent side */
  .card-agent {
    position: absolute; left: 118px; top: 470px;
    width: 662px; height: 368px;
    background: var(--paper);
    border: 1px solid var(--card-edge);
    box-shadow: 0 2px 6px rgba(0,0,0,.15);
    overflow: hidden;
  }
  .card-agent .title {
    position: absolute; left: 36px; top: 86px;
    font-size: 34px; font-weight: 400; color: var(--ink); white-space: nowrap;
  }
  .card-agent .title .role { font-size: 28px; }
  .card-agent .crop-rule {
    position: absolute; left: 36px; top: 132px; width: 256px; height: 26px;
  }
  .card-agent .contact {
    position: absolute; left: 36px; top: 280px;
    font-size: 21px; line-height: 1.35; color: var(--ink);
  }
  .contact .label { color: var(--racing-red); }
  .card-agent .horse-sketch {
    position: absolute; left: 330px; top: 64px; width: 332px; height: 304px;
    background: linear-gradient(160deg, var(--paper) 0%, var(--sketch-pink) 55%, #e2a9a1 100%);
    border-radius: 40% 30% 0 0 / 35% 30% 0 0;
  }

  /* Wordmark lockup */
  .lockup {
    position: absolute; left: 44px; top: 1006px;
  }
  .lockup .name {
    font-size: 74px; font-weight: 500; color: var(--ink); line-height: 1; white-space: nowrap;
  }
  .lockup .role {
    font-size: 44px; color: var(--racing-red); margin: 14px 0 0 146px; line-height: 1;
  }
  .lockup-sketch {
    position: absolute; left: 620px; top: 836px; width: 340px; height: 364px;
    background: linear-gradient(160deg, var(--backdrop) 0%, var(--sketch-pink) 50%, #d99b91 100%);
    border-radius: 45% 35% 0 0 / 35% 30% 0 0;
  }
</style>
</head>
<body>

<section class="card-jockeys">
  <div class="horse-sketch" role="img" aria-label="Sketched racehorse with rider, tone-on-tone red"></div>
  <h2 class="heading">Jockeys</h2>
  <svg class="crossed-crops" viewBox="0 0 64 64" aria-hidden="true">
    <g stroke="#ffffff" stroke-width="2" stroke-linecap="round">
      <line x1="6" y1="4" x2="58" y2="60"/>
      <line x1="58" y1="4" x2="6" y2="60"/>
    </g>
  </svg>
  <div class="jockey jockey-left">
    <div class="name">Everett Kline</div>
    <div class="weight">112 lbs</div>
  </div>
  <div class="jockey jockey-right">
    <div class="name">Tobias Renwick</div>
    <div class="weight">114 lbs</div>
  </div>
</section>

<section class="card-agent">
  <div class="horse-sketch" role="img" aria-label="Red line sketch of a racehorse with rider"></div>
  <h1 class="title">Garrett Lindqvist - <span class="role">Jockey Agent</span></h1>
  <svg class="crop-rule" viewBox="0 0 256 26" aria-hidden="true">
    <rect x="0" y="3" width="44" height="7" fill="#a51f24"/>
    <rect x="44" y="5" width="190" height="3" fill="#a51f24"/>
    <rect x="234" y="2" width="22" height="9" fill="#a51f24"/>
    <path d="M6 10 C4 20, 24 22, 30 12" fill="none" stroke="#a51f24" stroke-width="1.5"/>
  </svg>
  <div class="contact">
    <p><span class="label">mob.</span> (614) 382 7291</p>
    <p><span class="label">e-mail.</span> garrettplindqvist7mailhub.example</p>
  </div>
</section>

<div class="lockup-sketch" role="img" aria-label="Red line sketch of a racehorse with rider"></div>
<div class="lockup">
  <div class="name">Garrett Lindqvist</div>
  <div class="role">Jockey Agent</div>
</div>

</body>
</html>
```